Almost finish design need new idea for a particular area

Hi guys,
The product is baby wet wipe. I m happy with all area, except the side that locate at the side of the product (which I colored in Yellow)
I feel that consumer can not read the stuff easy (fixed stuffs that I tick in Red, no need to change), so I try to surround it by some kind of cloudy effect, but I still not happy, and would expect some other better ideas.
So the task is simple: to create a background for this side surface that can help people read the stuff inside easy. Personally, I think it should look simple, so it will not overshadow the rest main design. But you could try any ideas if you think it will match the whole design.
I m also attached a photo with 2 example of ideas, in which they totally understand my need, but some how still not match my product taste.
So therefore, I decide to come here, to open a contest.
I hope a designer in here could come up with a nice idea.
Thank you for reading this contest.
Ps: Here is google drive link, in case attached file can not open
https://files.plinkvault.net/shared/boxes/4kqzTmRw8PnYd2LsHcVbXe7uJfG3Qa?view=public

```html
<!DOCTYPE html>
<html lang="vi">
<head>
<meta charset="utf-8">
<title>Nuvie wet wipes – side panel options</title>
<link href="https://fonts.googleapis.com/css2?family=Baloo+2:wght@600;700&family=Open+Sans:wght@400&display=swap" rel="stylesheet">
<style>
  :root {
    --stage: #3a393b;
    --label: #ffffff;
    --panel: #ffffff;
    --aqua-soft: #b3e2e5;
    --aqua-text: #2a9fa0;
    --deep-teal: #15524f;
    --cloud: #c4e7ef;
    --art-mint: #d6efec;
    --art-line: #8fd0c6;
  }
  * { margin: 0; padding: 0; box-sizing: border-box; }
  html, body { width: 1200px; height: 631px; overflow: hidden; background: var(--stage); }
  .board {
    position: relative; width: 1200px; height: 631px;
    display: flex; justify-content: center; align-items: center; gap: 30px;
  }
  .option { display: flex; flex-direction: column; align-items: center; gap: 20px; }
  .option-title {
    font-family: "Open Sans", sans-serif; font-weight: 400;
    font-size: 30px; color: var(--label); letter-spacing: 0.5px;
  }
  .side-panel {
    position: relative; width: 540px; height: 160px;
    background: var(--panel); overflow: hidden;
    font-family: "Baloo 2", sans-serif;
  }
  .side-panel--glow {
    background: radial-gradient(ellipse 52% 62% at 50% 50%, var(--aqua-soft) 55%, var(--panel) 100%);
    color: var(--aqua-text);
  }
  .side-panel--cloud { color: var(--deep-teal); }
  .cloud-band {
    position: absolute; left: 0; top: 0; width: 100%; height: 34px;
    background: linear-gradient(180deg, var(--cloud) 70%, rgba(196,231,239,0));
  }
  .animal-art {
    position: absolute; bottom: 0;
    background: linear-gradient(180deg, var(--art-mint), rgba(143,208,198,0.55));
    border-radius: 14px 14px 0 0;
  }
  .animal-art--left { left: 4px; width: 170px; height: 100px; }
  .animal-art--right { right: 4px; width: 118px; height: 70px; }
  .brand-block {
    position: absolute; top: 42px; width: 140px; text-align: center; line-height: 1;
  }
  .side-panel--glow .brand-block { left: 120px; }
  .side-panel--cloud .brand-block { left: 128px; top: 44px; }
  .brand-name { font-weight: 700; font-size: 46px; letter-spacing: -0.5px; display: block; }
  .brand-tag { font-weight: 600; font-size: 21px; display: block; margin-top: 6px; }
  .info-block {
    position: absolute; top: 40px; width: 170px; text-align: center; line-height: 1;
  }
  .side-panel--glow .info-block { left: 272px; }
  .side-panel--cloud .info-block { left: 272px; top: 42px; }
  .count { display: inline-flex; align-items: flex-start; gap: 3px; }
  .count-num { font-weight: 700; font-size: 27px; }
  .count-meta { display: flex; flex-direction: column; text-align: left; padding-top: 3px; }
  .count-unit { font-weight: 600; font-size: 12px; line-height: 1; }
  .count-size { font-family: "Open Sans", sans-serif; font-size: 6px; line-height: 1.4; }
  .product-type { display: block; font-weight: 600; font-size: 15px; margin-top: 6px; }
  .claim { display: block; font-weight: 600; font-size: 20px; margin-top: 8px; }
</style>
</head>
<body>
<main class="board">
  <section class="option">
    <h2 class="option-title">Option-01</h2>
    <div class="side-panel side-panel--glow">
      <div class="brand-block">
        <span class="brand-name">Nuvie</span>
        <span class="brand-tag">Super thick</span>
      </div>
      <div class="info-block">
        <span class="count"><span class="count-num">60</span><span class="count-meta"><span class="count-unit">miếng</span><span class="count-size">20 x 15 cm</span></span></span>
        <span class="product-type">Khăn giấy ướt</span>
        <span class="claim">Day hon, sach hon</span>
      </div>
    </div>
  </section>

  <section class="option">
    <h2 class="option-title">Option-02</h2>
    <div class="side-panel side-panel--cloud">
      <div class="cloud-band" role="img" aria-label="Soft light-blue cloud border along the top edge"></div>
      <div class="animal-art animal-art--left" role="img" aria-label="Line-art baby animals: hippo, giraffe and crocodile in mint tones"></div>
      <div class="animal-art animal-art--right" role="img" aria-label="Line-art baby elephant and lion in mint tones"></div>
      <div class="brand-block">
        <span class="brand-name">Nuvie</span>
        <span class="brand-tag">Super thick</span>
      </div>
      <div class="info-block">
        <span class="count"><span class="count-num">60</span><span class="count-meta"><span class="count-unit">miếng</span><span class="count-size">20 x 15 cm</span></span></span>
        <span class="product-type">Khăn giấy ướt</span>
        <span class="claim">Day hon, sach hon</span>
      </div>
    </div>
  </section>
</main>
</body>
</html>
```